Wendorf Legal: Sole Practitioner Law Firm seeking corporate branding drawing on unique bush setting

I need a logo, stationary and business card design for my law firm. I will be practising as a sole practitioner specialising in corporate, commercial, finance, migration and agriculture law. Having left my corporate job in the city and relocated our family to our farm in regional Western Australia, I would like the corporate design for my company to be crisp, stylish, concise and uncomplicated. The law firm is called "Wendorf Legal" because we have a colony of the endangered Carnaby Black Cockatoos living in the bush behind our homestead (which is also my office). I will travel to clients rather than have them visit me. I would like to see a stylised image of the bird with some Australian native bush included in the design, either as a background image on the back of the card. A separate brief has been created for the logo and stationary though I hope all 3 pieces of work will "marry". The final design should communicate clarity of vision, efficiency, compassion and solution/ outcome focused. I prefer to have the business cards printed on card with a bit of texture and substance. I will try not to use laminated card as I consider it feels "plastic and commoditised" which is inconsistent with the image and feel of the business I intend creating. Please see attached brief for further details of the design brief.

Target Market(s)

Agriculture and Horticulture companies, Farmers, Family offices and estates, banks, insurance companies, individuals wishing to migrate to Australia

Industry/Entity Type

Legal

Contact Information for Business Card

Harriet Dunbar-Kelso
LLB (Hons), BSc., MEc.
Legal Practitioner and Director

WENDORF LEGAL PTY LTD
PO Box 273, Yarrowind WA 6057
Ph: 0472 918205
Email: harrietdk@quillnet.com

Solicitor admitted to practice in the Senior Bench Tribunal of Western Australia, England and Wales, NSW, and Registered Practitioner of the Apex Bench of Australia

Logo Text

WENDORF LEGAL: Client Focused Commercial Legal Solutions

Font styles to use
Other font styles liked:
• Verlag

Colors
ec1f27
fbee3d
9bcb3c
ffffff
1b1b1b
c4c4c4

Requirements
Must have
• A look and feel of quality, conservatism, adventure
Nice to have
• A stylised image of a Carnaby Cockatoo and Australian flora as a background image or design on the back of the card.
Should not have
• Clutter, cartoons

```html
<!DOCTYPE html>
<html lang="en">
<head>
<meta charset="utf-8">
<title>Wendorf Legal — Business Card</title>
<link rel="stylesheet" href="https://fonts.googleapis.com/css2?family=Open+Sans:wght@400;600&display=swap">
<style>
  :root {
    --page: #e6e3de;
    --card: #141414;
    --medallion: #1a1a1a;
    --gold: #d9a53a;
    --gold-light: #f5d27a;
    --gold-deep: #a8741f;
    --gold-shadow: #3a2a10;
    --ink: #ffffff;
    --ink-soft: #e8e8e8;
  }
  * { margin: 0; padding: 0; box-sizing: border-box; }
  html, body {
    width: 1117px;
    height: 1200px;
    overflow: hidden;
    background: var(--page);
  }
  .canvas {
    position: relative;
    width: 1117px;
    height: 1200px;
  }
  .card {
    position: absolute;
    left: 178px;
    width: 760px;
    height: 452px;
    background: radial-gradient(ellipse at center, #1e1e1e 0%, var(--card) 70%);
    box-shadow: 0 6px 18px rgba(0,0,0,0.25);
  }
  .card--front { top: 160px; }
  .card--back { top: 658px; }

  .card__frame {
    position: absolute;
    inset: 46px 46px 45px 46px;
    border: 2px solid var(--gold);
  }

  .front__text {
    position: absolute;
    left: 0;
    width: 100%;
    text-align: center;
    font-family: "Open Sans", sans-serif;
    font-weight: 400;
    color: var(--ink);
  }
  .holder-name {
    top: 82px;
    font-size: 28px;
    letter-spacing: 3px;
  }
  .holder-credentials {
    top: 122px;
    font-size: 15.5px;
    letter-spacing: 1.5px;
    line-height: 24px;
    color: var(--ink-soft);
  }
  .firm-name {
    top: 204px;
    font-size: 33px;
    letter-spacing: 4px;
  }
  .firm-rule {
    position: absolute;
    top: 246px;
    left: 120px;
    width: 520px;
    height: 2px;
    background: linear-gradient(90deg, var(--gold-deep), var(--gold-light), var(--gold-deep));
  }
  .contact-line {
    font-size: 16px;
    color: var(--ink-soft);
  }
  .contact-address { top: 274px; }
  .contact-phone { top: 315px; }
  .contact-email { top: 356px; }

  .back__pattern {
    position: absolute;
    inset: 48px 46px 46px 46px;
    border: 2px solid var(--gold);
    background: radial-gradient(ellipse at center, var(--gold-light) 0%, var(--gold) 40%, var(--gold-deep) 75%, var(--gold-shadow) 100%);
  }
  .back__medallion {
    position: absolute;
    left: 50%;
    top: 50%;
    width: 236px;
    height: 236px;
    margin: -118px 0 0 -118px;
    border-radius: 50%;
    background: var(--medallion);
  }
</style>
</head>
<body>
<main class="canvas">
  <section class="card card--front" aria-label="Business card front">
    <div class="card__frame"></div>
    <p class="front__text holder-name">HARRIET DUNBAR-KELSO</p>
    <p class="front__text holder-credentials">LLB (HONS), BSC., MEC.<br>LEGAL PRACTITIONER AND DIRECTOR</p>
    <p class="front__text firm-name">WENDORF LEGAL PTY LTD</p>
    <div class="firm-rule"></div>
    <p class="front__text contact-line contact-address">PO Box 273, Yarrowind WA 6057</p>
    <p class="front__text contact-line contact-phone">Phone: 0472 918205</p>
    <p class="front__text contact-line contact-email">Email: harrietdk@quillnet.com</p>
  </section>

  <section class="card card--back" aria-label="Business card back">
    <div class="back__pattern" role="img" aria-label="Gold ornamental pattern area surrounding a plain dark circular medallion">
      <div class="back__medallion"></div>
    </div>
  </section>
</main>
</body>
</html>
```